Editorial Website Design for High-End Custom Millwork Firm

Design (no development) for a 5-7 page website for a high-end custom architectural millwork firm. Editorial, magazine-quality aesthetic — think Dwelling Quarterly and top-tier millwork studios (Owen Tallard, Vorko). Full brief, reference sites, and project photography attached. We have uploaded a sample of our photography to use in your design. PLEASE READ PDF DOCUMENT BRIEF!!!

```html
<!DOCTYPE html>
<html lang="en">
<head>
<meta charset="utf-8">
<title>Halvard Millwork — Website Design</title>
<link href="https://fonts.googleapis.com/css2?family=Newsreader:opsz,wght@6..72,400;6..72,500&family=Inter:wght@400;500;600&display=swap" rel="stylesheet">
<style>
:root{
  --board:#1d1a1a;
  --page:#f6f2ec;
  --sand:#ede6dc;
  --card:#ebe3d7;
  --ink:#2a231f;
  --muted:#8b8076;
  --line:#cfc4b6;
  --brown:#7a5238;
  --brown-dark:#5a3b27;
  --cream:#fbf8f3;
  --footer:#8b6242;
}
*{margin:0;padding:0;box-sizing:border-box}
html,body{width:1200px;height:2555px;overflow:hidden;background:var(--board)}
body{position:relative;font-family:"Inter",sans-serif;color:var(--ink)}
.a{position:absolute}
.serif{font-family:"Newsreader",serif;font-weight:400;letter-spacing:-.01em}
.photo{position:absolute;border-radius:2px}
.desk{position:absolute;left:199px;top:96px;width:365px;height:2282px;background:var(--page);overflow:hidden}
.mob{position:absolute;left:669px;top:104px;width:89px;height:2224px;background:var(--page);overflow:hidden;border-radius:6px}
.eyebrow{font-size:2.2px;letter-spacing:.12em;text-transform:uppercase;color:var(--muted);font-weight:500}
.body{font-size:2.7px;line-height:4.3px;color:var(--muted)}
.btn{position:absolute;background:var(--brown);color:#fff;font-size:2.6px;display:flex;align-items:center;justify-content:center;border-radius:1px;font-weight:500}
.btn.ghost{background:transparent;color:var(--ink);border:.5px solid var(--ink)}
.center{text-align:center;left:0;right:0}
.card{position:absolute;background:var(--card);border-radius:2px;padding:0 9px}
.card h4{position:absolute;top:18px;left:9px;font-size:5.4px;font-weight:500}
.card p{position:absolute;top:30px;left:9px;right:9px}
.card .more{position:absolute;top:60px;left:9px;font-size:2.5px;color:var(--ink)}
.card.dark{background:linear-gradient(135deg,#a27554,#6e4a33);color:#fff}
.card.dark h4,.card.dark .more{color:#fff}
.card.dark p{color:#f0e2d4}
.badge{position:absolute;background:#3b3430;border-radius:1px}
.round{position:absolute;border-radius:50%}
.step-num{width:7px;height:7px;border-radius:50%;background:var(--brown);color:#fff;font-size:3px;display:flex;align-items:center;justify-content:center}
.step h5{font-size:4.4px;font-weight:500;margin:7px 0 2px}
.tab{position:absolute;height:9px;font-size:2.4px;display:flex;align-items:center;justify-content:center;border-radius:1px;background:#e3dace;color:var(--muted)}
.tab.on{background:var(--brown);color:#fff}
.quote{position:absolute;background:#efe8dd;border-radius:2px;padding:8px}
.stars{color:#c98d2e;font-size:3.5px;letter-spacing:.3px}
.post{position:absolute;background:#fff;border-radius:2px;overflow:hidden;box-shadow:0 0 0 .5px #e5ddd2}
.post h6{font-family:"Newsreader",serif;font-weight:400;font-size:3.6px;line-height:4.4px;margin:5px 5px 3px}
.post p{margin:0 5px}
.post .more{font-size:2.3px;margin:4px 5px}
.foot h6{font-size:4px;font-weight:600;color:#fff;margin-bottom:5px}
.foot li{list-style:none;font-size:2.5px;line-height:4.6px;color:#f1e4d6}
.m-eyebrow{font-size:1.6px;letter-spacing:.1em;text-transform:uppercase;color:var(--muted)}
.m-body{font-size:1.9px;line-height:2.9px;color:var(--muted)}
.m-card{position:absolute;left:6px;width:77px;background:var(--card);border-radius:1.5px;padding:8px 6px}
.m-card h4{font-size:3px;font-weight:500;margin-bottom:3px}
</style>
</head>
<body>

<!-- Desktop page -->
<main class="desk">

  <header class="a" style="left:0;top:0;width:365px;height:22px">
    <div class="a serif" style="left:21px;top:4px;font-size:7.5px;font-weight:500">Halvard Millwork</div>
    <nav class="a" style="left:185px;top:8px;display:flex;gap:8px;font-size:2.6px">
      <span>Home</span><span>Projects</span><span>Services</span><span>About</span><span>Journal</span><span>Contact</span>
    </nav>
    <div class="btn" style="left:311px;top:6px;width:34px;height:9px">Start a Project</div>
  </header>

  <section class="a" style="left:13px;top:29px;width:338px;height:179px">
    <div class="photo" role="img" aria-label="Modern atrium with glass-railed staircase and slatted timber feature wall" style="inset:0;background:linear-gradient(90deg,#f2ede7 0%,#ebe5dd 30%,#d8cfc4 48%,#c79f78 66%,#9f7350 78%,#5f6a52 90%,#ece7e1 100%)"></div>
    <div class="a eyebrow" style="left:17px;top:32px">Serving commercial &amp; residential clients throughout the southeast</div>
    <h1 class="a serif" style="left:17px;top:34px;width:165px;font-size:14.5px;line-height:19.5px">Architectural Millwork Crafted Without Compromise</h1>
    <p class="a body" style="left:17px;top:92px;width:105px">For more than three decades, Halvard Millwork has partnered with architects, designers, builders and homeowners to create exceptional commercial interiors and bespoke residential pieces — crafted to the highest standard.</p>
    <div class="btn" style="left:17px;top:125px;width:38px;height:8px">Start a Project</div>
    <div class="btn ghost" style="left:65px;top:125px;width:43px;height:8px">Our Capabilities</div>
    <div class="badge" style="left:17px;top:146px;width:23px;height:16px"></div>
    <div class="badge" style="left:315px;top:117px;width:11px;height:11px;border-radius:2px"></div>
    <div class="badge" style="left:315px;top:137px;width:11px;height:11px;border-radius:2px"></div>
    <div class="badge" style="left:315px;top:157px;width:11px;height:11px;border-radius:2px"></div>
  </section>

  <section class="a" style="left:13px;top:224px;width:338px;height:80px">
    <div class="eyebrow">About Halvard Millwork</div>
    <h2 class="a serif" style="left:0;top:6px;width:130px;font-size:13px;line-height:17.5px">Craftsmanship Built Around Every Detail.</h2>
    <div class="a" style="left:144px;top:1px;width:.6px;height:68px;background:var(--line)"></div>
    <p class="a body" style="left:168px;top:0;width:170px">Since 1988, Halvard Millwork has earned a reputation for producing architectural millwork that meets the highest standards of quality, precision, and durability. Every project is designed, engineered, fabricated, and finished within our Ashford facility, allowing complete control from concept through installation.<br>Our firm was established in 1988 and is located in historic Ashford. We are a family-owned business with a long tradition of employee participation. We draw on the area's history of fine furniture making and have attracted skilled craftsmen from across the country. With an average of twelve years employment, our truly dedicated staff is our strongest asset. Our family-like atmosphere has helped us grow not only in size but in quality and complexity of work as well.</p>
    <div class="btn ghost" style="left:168px;top:65px;width:42px;height:9px">Learn Our Story →</div>
  </section>

  <div class="photo" role="img" aria-label="Two craftsmen reviewing drawings on a workshop bench" style="left:13px;top:308px;width:338px;height:125px;background:linear-gradient(120deg,#cbb89c,#8c7258 45%,#4f4036 75%,#b49a7a)"></div>

  <section class="a" style="left:0;top:460px;width:365px;height:250px">
    <div class="a eyebrow center" style="text-align:center;top:2px">Our Services</div>
    <h2 class="a serif center" style="top:6px;text-align:center;font-size:12.5px">From Design Intent To Final Installation</h2>
    <p class="a body" style="left:82px;top:26px;width:200px;text-align:center">Whether fabricating custom reception desks, luxury hotel millwork, executive boardrooms, university interiors, or bespoke residential cabinetry, our experienced team delivers exceptional craftsmanship throughout every phase of production.</p>
    <div class="card" style="left:13px;top:51px;width:109px;height:83px"><h4>Architectural Millwork</h4><p class="body">Lorem ipsum dolor sit amet, consectetur adipiscing elit, sed do eiusmod tempor incididunt ut labore et dolore magna aliqua. Ut enim ad minim veniam, quis nostrud exercitation ullamco laboris nisi.</p><span class="more">Read More →</span></div>
    <div class="card dark" role="img" aria-label="Upholstered panel detail in warm leather tones" style="left:127px;top:51px;width:109px;height:83px"><h4>Upholstery Solutions</h4><p class="body">Lorem ipsum dolor sit amet, consectetur adipiscing elit, sed do eiusmod tempor incididunt ut labore et dolore magna aliqua. Ut enim ad minim veniam, quis nostrud exercitation ullamco laboris nisi.</p><span class="more">Read More →</span></div>
    <div class="card" style="left:241px;top:51px;width:110px;height:83px"><h4>Metal Fabrication</h4><p class="body">Lorem ipsum dolor sit amet, consectetur adipiscing elit, sed do eiusmod tempor incididunt ut labore et dolore magna aliqua. Ut enim ad minim veniam, quis nostrud exercitation ullamco laboris nisi.</p><span class="more">Read More →</span></div>
    <div class="card" style="left:13px;top:140px;width:109px;height:82px"><h4>Custom Cabinetry</h4><p class="body">Lorem ipsum dolor sit amet, consectetur adipiscing elit, sed do eiusmod tempor incididunt ut labore et dolore magna aliqua. Ut enim ad minim veniam, quis nostrud exercitation ullamco laboris nisi.</p><span class="more">Read More →</span></div>
    <div class="card" style="left:127px;top:140px;width:109px;height:82px"><h4>Interior Installations</h4><p class="body">Lorem ipsum dolor sit amet, consectetur adipiscing elit, sed do eiusmod tempor incididunt ut labore et dolore magna aliqua. Ut enim ad minim veniam, quis nostrud exercitation ullamco laboris nisi.</p><span class="more">Read More →</span></div>
    <div class="card" style="left:241px;top:140px;width:110px;height:82px"><h4>Commercial Interiors</h4><p class="body">Lorem ipsum dolor sit amet, consectetur adipiscing elit, sed do eiusmod tempor incididunt ut labore et dolore magna aliqua. Ut enim ad minim veniam, quis nostrud exercitation ullamco laboris nisi.</p><span class="more">Read More →</span></div>
    <div class="btn" style="left:156px;top:234px;width:53px;height:10px">Explore Capabilities</div>
  </section>

  <section class="a" style="left:0;top:730px;width:365px;height:120px">
    <div class="a eyebrow" style="left:13px;top:18px">Why Choose Us</div>
    <h2 class="a serif" style="left:13px;top:21px;width:140px;font-size:12px;line-height:17.5px">Built To The Highest Industry Standards</h2>
    <p class="a body" style="left:13px;top:58px;width:112px">Whether fabricating custom reception desks, luxury hotel millwork, executive boardrooms, university interiors, or bespoke residential cabinetry, our experienced team delivers exceptional craftsmanship throughout every phase.</p>
    <div class="btn" style="left:13px;top:87px;width:52px;height:9px">Explore Capabilities</div>
    <div class="a" style="left:171px;top:2px;width:83px;height:51px;background:#d9d0c4;border-radius:2px;padding:12px 7px">
      <div style="font-size:4.6px;font-weight:500">30+ Years</div>
      <div class="body" style="width:50px">Trusted craftsmanship since 1988.</div>
      <div style="font-size:2.3px;margin-top:3px">Learn Our Story →</div>
    </div>
    <div class="photo" role="img" aria-label="Workshop interior with stacked hardwood" style="left:258px;top:1px;width:93px;height:59px;background:linear-gradient(135deg,#6d6259,#3d3632)"></div>
    <div class="a" style="left:265px;top:12px;width:75px;color:#fff"><div style="font-size:4.6px;font-weight:500">Premium Grade</div><div class="body" style="color:#ddd2c6">Meeting the highest quality benchmarks for architectural woodwork.</div><div style="font-size:2.3px;margin-top:3px">Learn Our Story →</div></div>
    <div class="photo" role="img" aria-label="Machined timber components on a work table" style="left:168px;top:56px;width:82px;height:59px;background:linear-gradient(135deg,#5a5049,#302a27)"></div>
    <div class="a" style="left:176px;top:72px;width:68px;color:#fff"><div style="font-size:4.6px;font-weight:500">Complete Manufacturing</div><div class="body" style="color:#ddd2c6">Engineering, fabrication, finishing, and installation under one roof.</div><div style="font-size:2.3px;margin-top:3px">Learn Our Story →</div></div>
    <div class="a" style="left:257px;top:65px;width:90px;height:50px;background:var(--brown);border-radius:2px;padding:12px 8px;color:#fff"><div style="font-size:4.6px;font-weight:500">Award Quality</div><div class="body" style="color:#ecdccb">Recognized for exceptional precision and enduring craftsmanship.</div><div style="font-size:2.3px;margin-top:3px">Learn Our Story →</div></div>
  </section>

  <section class="a" style="left:0;top:869px;width:365px;height:312px;background:var(--sand)">
    <div class="a eyebrow center" style="text-align:center;top:17px">Our Process</div>
    <h2 class="a serif center" style="text-align:center;top:22px;font-size:12px">From Concept To Precision Installation</h2>
    <p class="a body" style="left:100px;top:40px;width:165px;text-align:center">Every project follows a carefully managed four-step process that ensures exceptional craftsmanship, seamless coordination, and flawless execution.</p>
    <div class="photo" role="img" aria-label="Craftsman assembling a cabinet frame with power tools" style="left:136px;top:69px;width:98px;height:71px;background:linear-gradient(135deg,#c9a984,#6e5644 60%,#3b3330)"></div>
    <div class="photo" role="img" aria-label="Finished white kitchen with timber island" style="left:37px;top:143px;width:99px;height:70px;background:linear-gradient(135deg,#f3ede4,#d8c2a3 60%,#a57b53)"></div>
    <div class="a" style="left:140px;top:143px;width:85px;height:70px;background:var(--cream);text-align:center">
      <div class="serif" style="margin-top:12px;font-size:12px;line-height:13px">Halvard<br>Millwork</div>
      <div class="btn" style="left:26px;top:49px;width:33px;height:6px;font-size:2px">Explore Our Process</div>
    </div>
    <div class="photo" role="img" aria-label="Worker fabricating a geometric lattice panel" style="left:229px;top:143px;width:99px;height:70px;background:linear-gradient(135deg,#c5c9cf,#8b8e92 55%,#4b4c50)"></div>
    <div class="photo" role="img" aria-label="Finishing booth with long timber boards" style="left:136px;top:217px;width:98px;height:70px;background:linear-gradient(135deg,#e4e1dc,#b7b1a9 60%,#7d756d)"></div>
    <div class="a step" style="left:42px;top:78px;width:80px"><div class="step-num">1</div><h5>Engineering</h5><p class="body">Every project begins with precise planning, detailed shop drawings, and technical coordination to ensure flawless execution.</p></div>
    <div class="a step" style="left:242px;top:78px;width:80px"><div class="step-num">2</div><h5>Fabrication</h5><p class="body">Expert craftsmen transform premium materials into custom millwork using advanced manufacturing and meticulous attention to detail.</p></div>
    <div class="a step" style="left:42px;top:228px;width:80px"><div class="step-num">4</div><h5>Installation</h5><p class="body">Our experienced installation teams deliver seamless, on-site execution with precision, care, and minimal disruption.</p></div>
    <div class="a step" style="left:242px;top:228px;width:80px"><div class="step-num">3</div><h5>Finishing</h5><p class="body">Each piece is carefully sanded, stained, painted, and inspected to achieve exceptional quality and lasting beauty.</p></div>
  </section>

  <section class="a" style="left:0;top:1192px;width:365px;height:372px">
    <div class="a eyebrow center" style="text-align:center;top:3px">Our Portfolio</div>
    <h2 class="a serif center" style="text-align:center;top:8px;font-size:12px">Showcasing Our Work</h2>
    <p class="a body" style="left:88px;top:26px;width:190px;text-align:center">Explore a selection of custom millwork and cabinetry projects crafted with precision, blending timeless design, exceptional craftsmanship, and lasting quality.</p>
    <div class="tab on" style="left:131px;top:42px;width:33px">COMMERCIAL</div>
    <div class="tab" style="left:169px;top:42px;width:33px">RESIDENTIAL</div>
    <div class="tab" style="left:207px;top:42px;width:28px">VIEW ALL</div>
    <div class="photo" role="img" aria-label="Hotel lobby with coffered ceiling, pendant lights and timber reception" style="left:13px;top:65px;width:163px;height:171px;background:linear-gradient(160deg,#d9c7ac,#7e5e42 45%,#3e2e24 80%,#6b4b33)"></div>
    <div class="photo" role="img" aria-label="Bright kitchen with wood cabinetry" style="left:179px;top:65px;width:84px;height:83px;background:linear-gradient(135deg,#efe6d8,#c9a57d)"></div>
    <div class="photo" role="img" aria-label="Bar counter with illuminated shelving" style="left:267px;top:65px;width:84px;height:83px;background:linear-gradient(135deg,#9b7656,#4c3626)"></div>
    <div class="photo" role="img" aria-label="Lounge with timber slat ceiling and blue seating" style="left:179px;top:152px;width:84px;height:84px;background:linear-gradient(135deg,#c79468,#6f5046 60%,#4e5a77)"></div>
    <div class="photo" role="img" aria-label="Dining space with patterned feature wall" style="left:267px;top:152px;width:84px;height:84px;background:linear-gradient(135deg,#c8a585,#8a5c44 60%,#5c6a4e)"></div>
    <div class="photo" role="img" aria-label="Commercial lounge with timber ceiling slats" style="left:13px;top:255px;width:169px;height:117px;background:linear-gradient(135deg,#b88459,#7a5640 55%,#3f5f73)"></div>
    <div class="photo" role="img" aria-label="Residential living room with custom cabinetry" style="left:182px;top:255px;width:169px;height:117px;background:linear-gradient(135deg,#ece5dc,#bfa58a 55%,#8c6b52)"></div>
    <div class="a" style="left:48px;top:295px;width:110px;padding:4px 6px;background:rgba(90,59,39,.75);color:#fff;text-align:center"><p style="font-size:2.6px;line-height:4px">From hospitality and higher education to corporate headquarters and luxury retail environments, Halvard delivers architectural millwork that meets the demanding standards of architects and general contractors.</p><div style="font-size:2.6px;margin-top:3px;font-weight:600">Commercial Projects →</div></div>
    <div class="a" style="left:228px;top:296px;width:100px;padding:4px 6px;background:rgba(90,59,39,.7);color:#fff;text-align:center"><p style="font-size:2.6px;line-height:4px">Thoughtfully crafted cabinetry and built-ins that bring timeless design and exceptional craftsmanship into private homes.</p><div style="font-size:2.6px;margin-top:3px;font-weight:600">Residential Projects →</div></div>
  </section>

  <section class="a" style="left:0;top:1592px;width:365px;height:145px">
    <div class="photo" role="img" aria-label="Craftsman cutting a geometric lattice panel" style="left:13px;top:0;width:138px;height:145px;background:linear-gradient(135deg,#8a8f89,#c7c4bd 50%,#4f5255)"></div>
    <div class="a eyebrow" style="left:157px;top:2px">Client Testimonials</div>
    <h2 class="a serif" style="left:157px;top:4px;width:195px;font-size:12px;line-height:17.5px">Trusted By Architects, Builders &amp; Designers</h2>
    <p class="a body" style="left:157px;top:43px;width:190px">For more than three decades, Halvard has partnered with leading architects, contractors, designers, and developers to deliver custom architectural millwork with precision and lasting quality.</p>
    <div class="quote" style="left:157px;top:65px;width:93px;height:80px"><div class="stars">★★★★★</div><p class="body" style="margin-top:3px">Halvard helped me by designing not only a beautiful, but a very functional kitchen and dining space. The team was pleased with all the steps of the process, from design to installation. They paid great attention to detail.</p><div class="round" style="left:8px;top:61px;width:8px;height:8px;background:#8aa3b5"></div><div class="a" style="left:20px;top:61px;font-size:2.6px;font-weight:600">Mara Lindqvist</div><div class="a" style="left:20px;top:65px;font-size:2.2px;color:var(--muted)">CEO, Company</div></div>
    <div class="quote" style="left:256px;top:65px;width:94px;height:80px"><div class="stars">★★★★★</div><p class="body" style="margin-top:3px">Halvard Millwork consistently delivers exceptional craftsmanship with unmatched attention to detail. Their team understands the importance of precision, communication, and schedules on every project.</p><div class="round" style="left:8px;top:61px;width:8px;height:8px;background:#8aa3b5"></div><div class="a" style="left:20px;top:61px;font-size:2.6px;font-weight:600">Mara Lindqvist</div><div class="a" style="left:20px;top:65px;font-size:2.2px;color:var(--muted)">CEO, Company</div></div>
    <svg class="a" style="left:353px;top:100px" width="5" height="6" viewBox="0 0 5 6"><path d="M1 .5 3.5 3 1 5.5" fill="none" stroke="#2a231f" stroke-width=".6"/></svg>
  </section>

  <section class="a" style="left:13px;top:1765px;width:338px;height:116px;background:#ece5da;border-radius:2px">
    <div class="photo" role="img" aria-label="Grand lobby with dark timber ceiling and display shelving" style="left:0;top:0;width:114px;height:116px;background:linear-gradient(150deg,#d8c6ac,#6e4f38 55%,#3a2b22)"></div>
    <div class="a eyebrow" style="left:138px;top:8px">Client Testimonials</div>
    <h2 class="a serif" style="left:138px;top:11px;width:150px;font-size:12px;line-height:17.5px">Let's Build Something Exceptional.</h2>
    <p class="a body" style="left:138px;top:48px;width:130px">Whether you're planning a commercial interior or a custom residential project, we'd welcome the opportunity to collaborate.</p>
    <div class="a" style="left:138px;top:71px;width:83px;height:11px;background:#fff;font-size:2.5px;color:var(--muted);padding:3.5px 4px">Email</div>
    <div class="btn" style="left:228px;top:71px;width:43px;height:11px">Contact Us</div>
    <div class="badge" style="left:140px;top:89px;width:18px;height:13px"></div>
    <div class="round" style="left:167px;top:89px;width:12px;height:12px;background:#36508a"></div>
    <div class="round" style="left:187px;top:89px;width:12px;height:12px;background:#3f6b47"></div>
  </section>

  <section class="a" style="left:0;top:1905px;width:365px;height:185px">
    <div class="a eyebrow center" style="text-align:center;top:3px">Latest Insights</div>
    <h2 class="a serif center" style="text-align:center;top:8px;font-size:12px">Insights &amp; Recent Projects</h2>
    <p class="a body" style="left:88px;top:27px;width:190px;text-align:center">Explore expert perspectives, project highlights, and behind-the-scenes stories showcasing the craftsmanship, innovation, and attention to detail behind every Halvard project.</p>
    <div class="post" style="left:15px;top:57px;width:75px;height:99px"><div role="img" aria-label="White kitchen with wood island" style="height:55px;background:linear-gradient(135deg,#f1ebe2,#cfb08a)"></div><h6>5 Architectural Millwork Trends Shaping Modern Commercial Interiors</h6><p class="body">Discover the latest materials, finishes and design approaches transforming modern offices.</p><div class="more">Read Article →</div></div>
    <div class="post" style="left:102px;top:57px;width:75px;height:99px"><div role="img" aria-label="Corporate lobby with blue accents" style="height:55px;background:linear-gradient(135deg,#dfe3e6,#7e8fa3 60%,#4f5a66)"></div><h6>Crafting a Custom Lobby for a Luxury Corporate Headquarters</h6><p class="body">Take an inside look at how our team engineered a sculptural reception space.</p><div class="more">Read Article →</div></div>
    <div class="post" style="left:189px;top:57px;width:75px;height:99px"><div role="img" aria-label="Lobby with coffered timber ceiling" style="height:55px;background:linear-gradient(150deg,#d2bfa2,#6b4c37 55%,#3a2b22)"></div><h6>From Design to Installation: The Journey of Custom Millwork</h6><p class="body">Follow a project from precise engineering and fabrication to seamless installation.</p><div class="more">Read Article →</div></div>
    <div class="post" style="left:276px;top:57px;width:75px;height:99px"><div role="img" aria-label="Warm timber shelving wall" style="height:55px;background:linear-gradient(135deg,#e3b57e,#a9713f)"></div><h6>Choosing the Right Wood Species for Lasting Architectural Millwork</h6><p class="body">A practical guide to grain, finish, durability and the character of each species.</p><div class="more">Read Article →</div></div>
    <svg class="a" style="left:6px;top:104px" width="5" height="6" viewBox="0 0 5 6"><path d="M4 .5 1.5 3 4 5.5" fill="none" stroke="#2a231f" stroke-width=".6"/></svg>
    <svg class="a" style="left:354px;top:104px" width="5" height="6" viewBox="0 0 5 6"><path d="M1 .5 3.5 3 1 5.5" fill="none" stroke="#2a231f" stroke-width=".6"/></svg>
    <div class="btn" style="left:160px;top:169px;width:44px;height:10px">View All Articles</div>
  </section>

  <footer class="a foot" role="img" aria-label="Footer set over a warm timber workshop backdrop" style="left:0;top:2112px;width:365px;height:170px;background:linear-gradient(120deg,#9a704d,#83593a 50%,#a17a58)">
    <div class="a serif" style="left:17px;top:18px;font-size:11px;letter-spacing:2px;color:#fff">HALVARD MILLWORK</div>
    <div class="a" style="left:17px;top:36px;font-size:2.2px;letter-spacing:.15em;color:#f1e4d6">CUSTOM ARCHITECTURAL MILLWORK &amp; CABINETRY</div>
    <div class="round" style="left:295px;top:32px;width:10px;height:10px;border:.6px solid #fff"></div>
    <div class="round" style="left:315px;top:32px;width:10px;height:10px;border:.6px solid #fff"></div>
    <div class="round" style="left:336px;top:32px;width:10px;height:10px;border:.6px solid #fff"></div>
    <div class="a" style="left:13px;top:62px;width:338px;height:.5px;background:rgba(255,255,255,.35)"></div>
    <div class="a" style="left:13px;top:68px"><h6>Company</h6><ul><li>Home</li><li>Projects</li><li>Services</li><li>About</li><li>Journal</li><li>Contact</li></ul></div>
    <div class="a" style="left:72px;top:68px"><h6>Projects</h6><ul><li>Commercial</li><li>Residential</li><li>Hospitality</li><li>Education</li><li>Luxury Homes</li><li>Corporate</li></ul></div>
    <div class="a" style="left:130px;top:68px"><h6>Capabilities</h6><ul><li>Architectural Millwork</li><li>Custom Cabinetry</li><li>Engineering</li><li>Finishing</li><li>Installation</li><li>Consulting</li></ul></div>
    <div class="a" style="left:189px;top:68px;width:60px"><h6>Contact</h6><ul><li>⌖ Address</li><li>118 Lantern Mill Road, Ashford</li><li>✆ Phone</li><li>(555) 014-2290</li><li>✉ Email</li><li>studio@halvardmillwork.com</li></ul></div>
    <div class="a" style="left:266px;top:68px;width:85px"><div style="font-size:2.2px;letter-spacing:.12em;color:#f1e4d6">NEWSLETTER</div><h6 style="font-size:5px;margin-top:2px">Contact Us</h6>
      <div style="height:8px;border:.5px solid rgba(255,255,255,.6);font-size:2.3px;color:#f1e4d6;padding:2.5px 3px;position:relative">Enter your email<span style="position:absolute;right:1px;top:1px;bottom:1px;background:#fff;color:var(--brown);padding:1px 3px">Send Now</span></div></div>
    <div class="badge" style="left:288px;top:108px;width:18px;height:12px;background:#4b4a2a"></div>
    <div class="round" style="left:314px;top:108px;width:12px;height:12px;background:#36508a"></div>
    <div class="round" style="left:335px;top:108px;width:12px;height:12px;background:#3f6b47"></div>
    <div class="a" style="left:13px;top:138px;width:338px;height:.5px;background:rgba(255,255,255,.35)"></div>
    <div class="a" style="left:17px;top:146px;font-size:2.4px;color:#f1e4d6">© 2025. All Rights Reserved.</div>
    <div class="a" style="left:321px;top:146px;font-size:2.4px;color:#f1e4d6">Back to top ↑</div>
  </footer>
</main>

<!-- Mobile page -->
<main class="mob">
  <header class="a" style="left:0;top:0;width:89px;height:20px">
    <div class="a serif" style="left:3px;top:11px;font-size:3.6px;font-weight:500">Halvard Millwork</div>
    <div class="btn" style="left:57px;top:12px;width:17px;height:4px;font-size:1.5px">Start a Project</div>
  </header>
  <div class="a" style="left:3px;top:20px;width:83px;height:147px;background:#f1ece5">
    <div class="a m-eyebrow" style="left:4px;top:15px">Serving the southeast</div>
    <h1 class="a serif" style="left:4px;top:18px;width:75px;font-size:6.4px;line-height:8.4px">Architectural Millwork Crafted Without Compromise</h1>
    <div class="btn" style="left:4px;top:69px;width:16px;height:4px;font-size:1.5px">Start a Project</div>
    <div class="btn ghost" style="left:23px;top:69px;width:16px;height:4px;font-size:1.5px">Capabilities</div>
    <div class="photo" role="img" aria-label="Atrium staircase with slatted timber wall" style="left:0;top:76px;width:83px;height:45px;background:linear-gradient(90deg,#e6dfd6,#c79f78 50%,#5f6a52)"></div>
    <div class="badge" style="left:4px;top:131px;width:12px;height:12px"></div>
    <p class="a m-body" style="left:30px;top:126px;width:50px">Decades of partnership with architects, designers and builders, crafting exceptional interiors.</p>
  </div>
  <div class="a m-eyebrow" style="left:3px;top:186px">About us</div>
  <h2 class="a serif" style="left:3px;top:189px;width:40px;font-size:5px;line-height:7.5px">Craftsmanship Built Around Every Detail.</h2>
  <p class="a m-body" style="left:48px;top:186px;width:38px">Since 1988, Halvard has produced architectural millwork of the highest quality, precision and durability, with every project built in our own facility.</p>
  <div class="btn ghost" style="left:48px;top:231px;width:20px;height:4px;font-size:1.5px">Our Capabilities</div>
  <div class="photo" role="img" aria-label="Craftsmen reviewing drawings" style="left:3px;top:246px;width:83px;height:45px;background:linear-gradient(120deg,#cbb89c,#6e5644 55%,#3d342e)"></div>

  <div class="a m-eyebrow center" style="text-align:center;top:304px">Our Services</div>
  <h2 class="a serif center" style="text-align:center;top:307px;font-size:4.6px;line-height:6.5px">From Design Intent To Final<br>Installation</h2>
  <p class="a m-body" style="left:10px;top:322px;width:69px;text-align:center">Reception desks, hotel millwork, boardrooms and bespoke residential cabinetry.</p>
  <div class="m-card" style="top:344px;height:40px"><h4>Architectural Millwork</h4><p class="m-body">Lorem ipsum dolor sit amet, consectetur adipiscing elit, sed do eiusmod tempor incididunt.</p></div>
  <div class="m-card" role="img" aria-label="Upholstered panel detail" style="top:392px;height:44px;background:linear-gradient(135deg,#a27554,#6e4a33);color:#fff"><h4>Upholstery Solutions</h4><p class="m-body" style="color:#ecdccb">Lorem ipsum dolor sit amet, consectetur adipiscing elit, sed do eiusmod tempor incididunt.</p></div>
  <div class="m-card" style="top:442px;height:41px"><h4>Metal Fabrication</h4><p class="m-body">Lorem ipsum dolor sit amet, consectetur adipiscing elit, sed do eiusmod tempor incididunt.</p></div>
  <div class="m-card" style="top:491px;height:41px"><h4>Custom Cabinetry</h4><p class="m-body">Lorem ipsum dolor sit amet, consectetur adipiscing elit, sed do eiusmod tempor incididunt.</p></div>
  <div class="m-card" style="top:541px;height:41px"><h4>Interior Installations</h4><p class="m-body">Lorem ipsum dolor sit amet, consectetur adipiscing elit, sed do eiusmod tempor incididunt.</p></div>
  <div class="m-card" style="top:590px;height:41px"><h4>Commercial Interiors</h4><p class="m-body">Lorem ipsum dolor sit amet, consectetur adipiscing elit, sed do eiusmod tempor incididunt.</p></div>
  <div class="btn" style="left:25px;top:644px;width:38px;height:4.5px;font-size:1.5px">Explore Capabilities</div>

  <h2 class="a serif" style="left:6px;top:669px;width:70px;font-size:4.6px;line-height:6.5px">Built To The Highest Industry Standards</h2>
  <p class="a m-body" style="left:6px;top:685px;width:60px">Exceptional craftsmanship throughout every phase of production.</p>
  <div class="btn" style="left:6px;top:704px;width:20px;height:4px;font-size:1.5px">Start a Project</div>
  <div class="a" style="left:6px;top:721px;width:37px;height:22px;background:#d9d0c4"></div>
  <div class="photo" role="img" aria-label="Workshop timber stacks" style="left:45px;top:721px;width:35px;height:22px;background:linear-gradient(135deg,#6d6259,#3d3632)"></div>
  <div class="photo" role="img" aria-label="Machined timber parts" style="left:6px;top:745px;width:37px;height:22px;background:linear-gradient(135deg,#5a5049,#302a27)"></div>
  <div class="a" style="left:45px;top:745px;width:35px;height:22px;background:var(--brown)"></div>

  <div class="a" style="left:0;top:776px;width:89px;height:130px;background:var(--sand)">
    <div class="a m-eyebrow center" style="text-align:center;top:5px">Our Process</div>
    <h2 class="a serif center" style="text-align:center;top:8px;font-size:4.4px;line-height:6px">From Concept To Precision<br>Installation</h2>
    <p class="a m-body" style="left:10px;top:22px;width:69px;text-align:center">A carefully managed four-step process.</p>
    <div class="photo" role="img" aria-label="Craftsman at cabinet frame" style="left:32px;top:45px;width:24px;height:18px;background:linear-gradient(135deg,#c9a984,#3b3330)"></div>
    <div class="photo" role="img" aria-label="White kitchen" style="left:6px;top:66px;width:24px;height:18px;background:linear-gradient(135deg,#f3ede4,#a57b53)"></div>
    <div class="a serif" style="left:33px;top:69px;width:22px;text-align:center;font-size:3.4px;line-height:3.6px">Halvard<br>Millwork</div>
    <div class="photo" role="img" aria-label="Lattice panel fabrication" style="left:58px;top:66px;width:24px;height:18px;background:linear-gradient(135deg,#c5c9cf,#4b4c50)"></div>
    <div class="photo" role="img" aria-label="Finishing booth" style="left:32px;top:87px;width:24px;height:18px;background:linear-gradient(135deg,#e4e1dc,#7d756d)"></div>
    <p class="a m-body" style="left:4px;top:45px;width:26px">Engineering: precise planning and drawings.</p>
    <p class="a m-body" style="left:59px;top:45px;width:26px">Fabrication: premium materials, crafted.</p>
    <p class="a m-body" style="left:4px;top:88px;width:26px">Installation: seamless on-site work.</p>
    <p class="a m-body" style="left:59px;top:88px;width:26px">Finishing: sanded, stained, inspected.</p>
    <div class="btn" style="left:26px;top:118px;width:36px;height:4.5px;font-size:1.5px">Explore Our Process →</div>
  </div>

  <div class="a m-eyebrow center" style="text-align:center;top:917px">Our Portfolio</div>
  <h2 class="a serif center" style="text-align:center;top:920px;font-size:4.6px">Showcasing Our Work</h2>
  <p class="a m-body" style="left:10px;top:930px;width:69px;text-align:center">Custom millwork and cabinetry crafted with precision.</p>
  <div class="tab on" style="left:8px;top:943px;width:20px;height:4px;font-size:1.3px">COMMERCIAL</div>
  <div class="tab" style="left:34px;top:943px;width:20px;height:4px;font-size:1.3px">RESIDENTIAL</div>
  <div class="tab" style="left:62px;top:943px;width:14px;height:4px;font-size:1.3px">VIEW ALL</div>
  <div class="photo" role="img" aria-label="Hotel lobby with coffered ceiling" style="left:3px;top:956px;width:83px;height:85px;background:linear-gradient(160deg,#d9c7ac,#7e5e42 45%,#3e2e24)"></div>
  <div class="photo" role="img" aria-label="Bright kitchen" style="left:3px;top:1044px;width:40px;height:40px;background:linear-gradient(135deg,#efe6d8,#c9a57d)"></div>
  <div class="photo" role="img" aria-label="Bar with shelving" style="left:46px;top:1044px;width:40px;height:40px;background:linear-gradient(135deg,#9b7656,#4c3626)"></div>
  <div class="photo" role="img" aria-label="Lounge with blue seating" style="left:3px;top:1086px;width:40px;height:40px;background:linear-gradient(135deg,#c79468,#4e5a77)"></div>
  <div class="photo" role="img" aria-label="Dining with feature wall" style="left:46px;top:1086px;width:40px;height:40px;background:linear-gradient(135deg,#c8a585,#5c6a4e)"></div>
  <div class="photo" role="img" aria-label="Commercial lounge with timber ceiling" style="left:0;top:1139px;width:89px;height:57px;background:linear-gradient(135deg,#b88459,#3f5f73)"></div>
  <div class="photo" role="img" aria-label="Residential living room cabinetry" style="left:0;top:1196px;width:89px;height:57px;background:linear-gradient(135deg,#ece5dc,#8c6b52)"></div>

  <div class="photo" role="img" aria-label="Craftsman cutting lattice panel" style="left:3px;top:1268px;width:83px;height:76px;background:linear-gradient(135deg,#8a8f89,#c7c4bd 50%,#4f5255)"></div>
  <h2 class="a serif" style="left:3px;top:1352px;width:83px;font-size:4.6px;line-height:6.5px">Trusted By Architects, Builders &amp; Designers</h2>
  <p class="a m-body" style="left:3px;top:1368px;width:80px">Partnering with architects and contractors for three decades.</p>
  <div class="a" style="left:3px;top:1390px;width:39px;height:42px;background:#efe8dd"></div>
  <div class="a" style="left:46px;top:1390px;width:40px;height:42px;background:#efe8dd"></div>

  <div class="a" style="left:3px;top:1446px;width:83px;height:45px;background:#ece5da">
    <h2 class="a serif" style="left:7px;top:5px;width:70px;font-size:4.6px;line-height:6.5px">Let's Build Something Exceptional.</h2>
    <div class="a" style="left:7px;top:30px;width:40px;height:4px;background:#fff"></div>
    <div class="btn" style="left:55px;top:30px;width:20px;height:4px;font-size:1.4px">Contact Us</div>
    <div class="badge" style="left:7px;top:37px;width:6px;height:5px"></div>
    <div class="round" style="left:16px;top:37px;width:5px;height:5px;background:#36508a"></div>
    <div class="round" style="left:24px;top:37px;width:5px;height:5px;background:#3f6b47"></div>
  </div>
  <div class="photo" role="img" aria-label="Grand lobby with timber ceiling" style="left:3px;top:1499px;width:83px;height:42px;background:linear-gradient(150deg,#d8c6ac,#3a2b22)"></div>

  <div class="a m-eyebrow center" style="text-align:center;top:1553px">Latest Insights</div>
  <h2 class="a serif center" style="text-align:center;top:1556px;font-size:4.6px">Insights &amp; Recent Projects</h2>
  <div class="post" style="left:5px;top:1585px;width:79px;height:110px"><div role="img" aria-label="White kitchen with wood island" style="height:60px;background:linear-gradient(135deg,#f1ebe2,#cfb08a)"></div><h6 style="font-size:3px;line-height:3.6px">5 Architectural Millwork Trends Shaping Modern Commercial Interiors</h6><p class="m-body">Materials and finishes transforming offices.</p></div>
  <div class="post" style="left:5px;top:1700px;width:79px;height:110px"><div role="img" aria-label="Corporate lobby with blue accents" style="height:60px;background:linear-gradient(135deg,#dfe3e6,#4f5a66)"></div><h6 style="font-size:3px;line-height:3.6px">Crafting a Custom Lobby for a Luxury Corporate Headquarters</h6><p class="m-body">Inside a sculptural reception space.</p></div>
  <div class="post" style="left:5px;top:1815px;width:79px;height:110px"><div role="img" aria-label="Lobby with coffered timber ceiling" style="height:60px;background:linear-gradient(150deg,#d2bfa2,#3a2b22)"></div><h6 style="font-size:3px;line-height:3.6px">From Design to Installation: The Journey of Custom Millwork</h6><p class="m-body">A project from drawings to install.</p></div>
  <div class="post" style="left:5px;top:1930px;width:79px;height:110px"><div role="img" aria-label="Warm timber shelving wall" style="height:60px;background:linear-gradient(135deg,#e3b57e,#a9713f)"></div><h6 style="font-size:3px;line-height:3.6px">Choosing the Right Wood Species for Lasting Architectural Millwork</h6><p class="m-body">Grain, finish and durability explained.</p></div>
  <div class="btn" style="left:33px;top:2049px;width:22px;height:4.5px;font-size:1.5px">Start a Project</div>

  <footer class="a foot" role="img" aria-label="Footer over timber workshop backdrop" style="left:0;top:2071px;width:89px;height:153px;background:linear-gradient(120deg,#9a704d,#83593a 50%,#a17a58)">
    <div class="a serif" style="left:0;right:0;text-align:center;top:14px;font-size:5px;letter-spacing:1px;color:#fff">HALVARD MILLWORK</div>
    <div class="round" style="left:31px;top:27px;width:6px;height:6px;border:.4px solid #fff"></div>
    <div class="round" style="left:41px;top:27px;width:6px;height:6px;border:.4px solid #fff"></div>
    <div class="round" style="left:51px;top:27px;width:6px;height:6px;border:.4px solid #fff"></div>
    <div class="a" style="left:8px;top:50px;font-size:2.4px;color:#fff;font-weight:600">Contact Us</div>
    <div class="a" style="left:8px;top:56px;width:72px;height:5px;border:.4px solid rgba(255,255,255,.6)"></div>
    <div class="a" style="left:8px;top:84px;font-size:2px;color:#fff;font-weight:600">Company</div>
    <div class="a m-body" style="left:8px;top:88px;color:#f1e4d6;width:22px">Home<br>Projects<br>Services<br>About<br>Journal<br>Contact</div>
    <div class="a" style="left:38px;top:84px;font-size:2px;color:#fff;font-weight:600">Contact</div>
    <div class="a m-body" style="left:38px;top:88px;color:#f1e4d6;width:44px">⌖ 118 Lantern Mill Road<br>Ashford<br>✆ (555) 014-2290<br>✉ studio@halvardmillwork.com</div>
    <div class="a m-body" style="left:8px;top:143px;color:#f1e4d6">© 2025. All Rights Reserved.</div>
    <div class="a m-body" style="left:68px;top:143px;color:#f1e4d6">Back to top</div>
  </footer>
</main>

</body>
</html>
```